BANNER FOR ONLINE CABINET COMPANY MAIN PAGE

Need 3 different banners for the main page. We are online platform for ordering cabinets, parts etc. online.
Website: bordaline.ca
A place where the banner will be placed: https://view.pelmoraclip.com/qTR7WkVbNHEa4
Banner size: 1344x399 pixels
****Clients should get the main point that they can order everything online through the website.

Industry/Entity Type

online cabinets and parts ordering

Requirements
Must have
• online ordering icons, vexaphone, laptop, desktop pc - so clients get an idea that this is web based service to order cabinets

```html
<!DOCTYPE html>
<html lang="en">
<head>
<meta charset="utf-8">
<title>Bordaline – Banner Set</title>
<link href="https://fonts.googleapis.com/css2?family=Jost:wght@400;500;600;700&family=Inter:wght@400;600;700&display=swap" rel="stylesheet">
<style>
:root{
  --sky-top:#74bbfa;
  --sky-bottom:#66a3f7;
  --shadow-blue:#6a86b4;
  --rose-top:#fb9c88;
  --rose-mid:#f47d92;
  --rose-bottom:#f78ea4;
  --teal:#6ac3c9;
  --teal-btn:#137f87;
  --olive:#7f9e0f;
  --olive-btn:#566b06;
  --olive-icon:#f2f58a;
  --tan:#c99b64;
  --tan-btn:#966224;
  --white:#ffffff;
  --nav-dark:#3b3e41;
  --header-grey:#e9eaeb;
  --ink:#1d1d1d;
  --order-green:#2cb34a;
}
*{margin:0;padding:0;box-sizing:border-box}
html,body{width:749px;height:1200px;overflow:hidden}
body{font-family:"Jost",sans-serif;color:var(--white)}
.canvas{position:relative;width:749px;height:1200px;overflow:hidden}

.showcase{position:absolute;left:0;top:0;width:749px;height:820px;
  background:linear-gradient(180deg,var(--sky-top) 0%,#a9d3fd 45%,var(--sky-bottom) 100%)}
.showcase-title{position:absolute;top:22px;width:100%;text-align:center;font-size:27px;font-weight:500;letter-spacing:.5px}
.showcase-size{position:absolute;top:60px;width:100%;text-align:center;font-size:14px;font-weight:500}

.banner{position:absolute;left:30px;width:690px;height:205px;display:flex;
  box-shadow:-5px 7px 0 var(--shadow-blue)}
.banner-one{top:109px}
.banner-two{top:348px}
.banner-three{top:587px}

.photo{height:100%}
.photo-bathroom{width:218px;background:linear-gradient(160deg,#8ea29c 0%,#7d918b 55%,#b7aa93 80%,#c9c6c2 100%)}
.photo-kitchen-white{flex:1;background:linear-gradient(180deg,#f3f2f0 0%,#e9e6e2 25%,#b88562 38%,#efeeec 55%,#f6f6f5 80%,#c79a6e 100%)}
.photo-kitchen-oak{width:510px;background:linear-gradient(170deg,#8e6c4c 0%,#7a5a3e 35%,#d9d7d3 55%,#b5b1aa 80%,#6b4f37 100%)}
.photo-sideboard{width:310px;background:linear-gradient(180deg,#eeedeb 0%,#e6e2dc 45%,#4b5157 62%,#3e4449 100%)}
.photo-dresser{flex:1;background:linear-gradient(180deg,#f2f1ee 0%,#ebe6df 50%,#f7f7f6 65%,#e3e3e2 100%)}

.promo{width:180px;height:100%;display:flex;flex-direction:column;align-items:center;padding-top:12px;text-align:center}
.promo-teal{background:var(--teal)}
.promo-olive{background:var(--olive)}
.promo-tan{background:var(--tan)}
.promo-heading{font-size:14.5px;line-height:16px;font-weight:400;letter-spacing:.2px}
.promo-heading strong{display:block;font-weight:600}
.devices{width:118px;height:66px;margin-top:16px}
.promo-olive .devices{color:var(--olive-icon)}
.promo-copy{font-size:8.6px;line-height:10px;margin-top:12px;padding:0 6px}
.order-btn{display:flex;align-items:center;justify-content:center;width:128px;height:30px;margin-top:auto;margin-bottom:11px;font-size:11px;letter-spacing:.4px}
.promo-teal .order-btn{background:var(--teal-btn)}
.promo-olive .order-btn{background:var(--olive-btn)}
.promo-tan .order-btn{background:var(--tan-btn)}

.preview{position:absolute;left:0;top:820px;width:749px;height:380px;
  background:linear-gradient(180deg,var(--rose-top) 0%,var(--rose-mid) 60%,var(--rose-bottom) 100%)}
.preview-title{position:absolute;top:22px;width:100%;text-align:center;font-size:19px;font-weight:500;letter-spacing:.3px}

.site{position:absolute;left:29px;top:66px;width:698px;height:302px;background:var(--white);font-family:"Inter",sans-serif;overflow:hidden}
.site-nav{height:18px;background:var(--nav-dark);display:flex;align-items:center;padding:0 10px;font-size:4.4px;gap:8px}
.site-brand{font-family:"Jost",sans-serif;font-size:7.5px;font-weight:600;padding-right:6px;border-right:1px solid #aaa}
.site-contact{background:#1f2123;padding:2px 5px;display:flex;gap:6px}
.site-menu{margin-left:auto;display:flex;align-items:center;gap:8px}
.site-order{background:var(--order-green);border-radius:5px;padding:1.5px 5px;font-weight:700}
.site-header{height:31px;background:var(--header-grey);text-align:center;color:var(--ink)}
.site-header h1{font-size:10.5px;font-weight:700;padding-top:3px;letter-spacing:.2px}
.site-header p{font-size:6.6px;color:#555;margin-top:3px}
.site .banner{position:relative;left:0;top:0;width:694px;height:210px;box-shadow:none}
.site .photo-bathroom{width:219px}
.site .promo{width:181px}
.carousel-dots{display:flex;justify-content:center;gap:5px;margin-top:3px}
.carousel-dots span{width:4px;height:4px;background:#cfcfcf}
.carousel-dots .is-active{background:#f39a1e}
.site-tagline{text-align:center;color:var(--ink);font-size:10.5px;font-weight:700;margin-top:12px;letter-spacing:.2px}
</style>
</head>
<body>
<div class="canvas">

  <svg width="0" height="0" style="position:absolute">
    <defs>
      <symbol id="devices-icon" viewBox="0 0 118 66">
        <g fill="none" stroke="currentColor" stroke-width="2.4" stroke-linejoin="round">
          <rect x="14" y="2" width="84" height="54" rx="3"/>
          <path d="M2 60 H100 V64 H4 Z" fill="currentColor"/>
          <rect x="70" y="17" width="36" height="45" rx="3" fill="var(--panel)"/>
          <rect x="90" y="26" width="20" height="36" rx="3" fill="var(--panel)"/>
        </g>
      </symbol>
    </defs>
  </svg>

  <section class="showcase">
    <h1 class="showcase-title">3 Banner Set- Mockup 1</h1>
    <p class="showcase-size">Banner size: 1344x399 pixels</p>

    <article class="banner banner-one">
      <div class="photo photo-bathroom" role="img" aria-label="Bathroom with floating oak vanity, tall shelf unit and mirror on a sage wall"></div>
      <div class="promo promo-teal" style="--panel:var(--teal)">
        <h2 class="promo-heading">ORDER YOUR<strong>CABINETS ONLINE</strong></h2>
        <svg class="devices"><use href="#devices-icon"/></svg>
        <p class="promo-copy">Create cutom cabinet for your home.<br>Order now using your phone/Laptop</p>
        <span class="order-btn">ORDER NOW</span>
      </div>
      <div class="photo photo-kitchen-white" role="img" aria-label="White kitchen island with walnut wall cabinets and pendant lights"></div>
    </article>

    <article class="banner banner-two">
      <div class="photo photo-kitchen-oak" role="img" aria-label="Kitchen with white shaker cabinets, oven, wood countertop and a leather chair by the window"></div>
      <div class="promo promo-olive" style="--panel:var(--olive)">
        <h2 class="promo-heading">CUSTOM<strong>KITCHEN CABINET</strong></h2>
        <svg class="devices"><use href="#devices-icon"/></svg>
        <p class="promo-copy">Make your kitchen more beautiful and useful. Order now from your Laptop/Phones.</p>
        <span class="order-btn">ORDER NOW</span>
      </div>
    </article>

    <article class="banner banner-three">
      <div class="photo photo-sideboard" role="img" aria-label="Dark grey sideboard with lamp, vase and woven baskets"></div>
      <div class="promo promo-tan" style="--panel:var(--tan)">
        <h2 class="promo-heading">CUSTOM CABINET<strong>ORDER ONLINE</strong></h2>
        <svg class="devices"><use href="#devices-icon"/></svg>
        <p class="promo-copy">you can now order online here your custom wall cabinet. Its simple and easy to order</p>
        <span class="order-btn">ORDER NOW</span>
      </div>
      <div class="photo photo-dresser" role="img" aria-label="White dresser with table lamp, frames and decor"></div>
    </article>
  </section>

  <section class="preview">
    <h2 class="preview-title">Showing Banner on your website</h2>

    <div class="site">
      <nav class="site-nav">
        <span class="site-brand">bordaline</span>
        <span>Get the size you need!</span>
        <span class="site-contact"><span>Call us (555) 014 2290</span><span>Mon-Fri 8AM - 4:30PM</span></span>
        <span class="site-menu">
          <span>CAD</span>
          <span class="site-order">ORDER NOW</span>
          <span>DESIGN &amp; QUOTE</span>
          <span>SAMPLES</span>
          <span>ABOUT</span>
          <span>CONTACT</span>
          <span>ARTICLES</span>
          <svg width="6" height="6" viewBox="0 0 10 10"><circle cx="4" cy="4" r="3" fill="none" stroke="#fff" stroke-width="1.2"/><path d="M6.2 6.2 9 9" stroke="#fff" stroke-width="1.2"/></svg>
          <span style="font-size:7px;font-weight:700">?</span>
          <svg width="7" height="7" viewBox="0 0 10 10"><circle cx="5" cy="3" r="2.2" fill="none" stroke="#fff"/><path d="M1 9.5c0-2.5 2-3.8 4-3.8s4 1.3 4 3.8" fill="none" stroke="#fff"/></svg>
          <svg width="8" height="7" viewBox="0 0 12 10"><path d="M0.5 1h2l1.5 6h6l1.5-4.5H3" fill="none" stroke="#fff"/><circle cx="5" cy="9" r=".8" fill="#fff"/><circle cx="9" cy="9" r=".8" fill="#fff"/></svg>
        </span>
      </nav>
      <header class="site-header">
        <h1>THE FIRST ONLINE CUSTOM CABINET’S MANUFACTURER</h1>
        <p>Order custom cabinets online with instant price calculator. No hidden fees, top quality warranty.</p>
      </header>

      <article class="banner">
        <div class="photo photo-bathroom" role="img" aria-label="Bathroom with floating oak vanity, tall shelf unit and mirror on a sage wall"></div>
        <div class="promo promo-teal" style="--panel:var(--teal)">
          <h2 class="promo-heading">ORDER YOUR<strong>CABINETS ONLINE</strong></h2>
          <svg class="devices"><use href="#devices-icon"/></svg>
          <p class="promo-copy">Create cutom cabinet for your home.<br>Order now using your phone/Laptop</p>
          <span class="order-btn">ORDER NOW</span>
        </div>
        <div class="photo photo-kitchen-white" role="img" aria-label="White kitchen island with walnut wall cabinets and pendant lights"></div>
      </article>

      <div class="carousel-dots"><span></span><span></span><span></span><span></span><span></span><span class="is-active"></span><span></span><span></span></div>
      <p class="site-tagline">EASY QUOTE &amp; ORDER</p>
    </div>
  </section>

</div>
</body>
</html>
```